VoRuBel Estates (New Napa Valley Cabernet) Website Design

We need a website design for our new company, VoRuBel Estates and the launch of our inaugural vintage of VoRuBel Napa Valley Cabernet. Here is our story:

2009 Napa Valley Cabernet Sauvignon
VoRuBel
Three friends, a passion for wine and a love of creating together fueled our development of VoRuBel Cabernet. As with most ardent endeavors, VoRuBel has been a project requiring the ultimate in patience, perseverance and commitment.

Our brand, VoRuBel is the phonetic spelling of our initials – Tessa, Lorna, and Stuart - and is pronounced VRB. Our logo, three wine glasses entwined, is the symbol of our friendship, the celebration of our families and our toast to the passionate desire to create remarkable wines from Napa Valley.

In every bottle of VoRuBel Cabernet Sauvignon, we hope you taste not only the richness and balanced flavors of the wine, but also the bond of our friendship.

From Tessa, Lorna and Stuart . . .
“We toast to all of life’s moments with you!”

We are launching our website and the eCom sales of our wine in October 2012. The website is our only means for soliciting orders. We have a bottle shot, a logo, some pictures and a wire frame and content draft. The wine is labeled and approved. We do not have a look, feel or architecture for our website. We will be making additional wines in the future but currently are releasing our 2009 VoRuBel Napa Valley Cabernet.

We are required to provide layered photo shop or word press design files to our eCom platform provider.

Thanks for your interest and ideas.

Wine drinkers, likely baby boomer age, largely CA located, higher income

Architecture

Must have
• Must have a store
Prefer not to reverse out the logo
Home page should feature some pictures, not heavy text

```html
<!DOCTYPE html>
<html lang="en">
<head>
<meta charset="utf-8">
<title>VoRuBel Estates – Napa Valley Cabernet</title>
<link rel="stylesheet" href="https://fonts.googleapis.com/css2?family=PT+Sans:wght@400;700&family=PT+Sans+Narrow:wght@700&family=Cormorant+Garamond:ital,wght@1,500&family=Arimo:wght@400;700&display=swap">
<style>
:root{
  --gold:#a66d1c;
  --gold-light:#c08a2c;
  --tab-top:#b97a10;
  --tab-bottom:#f2d21a;
  --ink:#111;
  --muted:#555;
  --footer:#0a0a0a;
  --panel:#e6e6e6;
  --buy:#6a0f18;
  --orange:#f08a00;
}
*{margin:0;padding:0;box-sizing:border-box}
html,body{width:1200px;height:854px;overflow:hidden;background:#fff}
body{font-family:"PT Sans",sans-serif;color:var(--ink);position:relative}
.hero-backdrop{position:absolute;left:0;top:0;width:1200px;height:326px;
  background:linear-gradient(180deg,#fff 0,#fff 70px,#ece6d6 100px,#d9cc9a 160px,#cfc58c 240px,#d8d0b0 326px)}
.brand{position:absolute;left:218px;top:44px;display:flex;align-items:center;gap:10px;
  font-family:"Cormorant Garamond",serif;font-style:italic;font-weight:500;font-size:36px;color:#2a2220}
.brand-dot{width:22px;height:22px;border-radius:50%;background:#bdbdbd}
.cart{position:absolute;left:814px;top:4px;width:201px;height:76px;background:#fbfbfb;border:1px solid #e2e2e2}
.cart-icon{position:absolute;left:26px;top:3px}
.cart-title{position:absolute;right:13px;top:4px;font-family:Arimo,sans-serif;font-weight:700;font-size:10.5px;color:#222}
.cart-bottles{position:absolute;left:18px;top:30px;display:flex;gap:2px}
.cart-bottles span{width:7px;height:28px;background:#777;border-radius:3px 3px 1px 1px}
.cart-total{position:absolute;right:15px;top:37px;font-family:Arimo,sans-serif;font-weight:700;font-size:14px}
.cart-links{position:absolute;left:0;right:0;bottom:3px;text-align:center;font-family:Arimo,sans-serif;font-weight:700;font-size:10.5px;color:#222}
.banner{position:absolute;left:196px;top:104px;width:834px;height:222px;border:2px solid #1a1a1a;
  background:linear-gradient(90deg,#4a2a20 0,#7a6050 25%,#6f8a58 40%,#3f6a30 60%,#2e4a22 75%,#1d1d1d 88%,#c9c1a4 100%)}
.nav{position:absolute;left:0;top:326px;width:1200px;height:30px;background:linear-gradient(180deg,var(--gold-light),var(--gold))}
.nav ul{list-style:none;position:absolute;left:0;top:0}
.nav li{position:absolute;top:5px;white-space:nowrap;font-family:"PT Sans Narrow",sans-serif;font-weight:700;font-size:15.5px;color:#fff;letter-spacing:.3px}
.content{position:absolute;left:0;top:356px;width:1200px;height:318px;background:linear-gradient(180deg,#e3e3e3 0,#fff 70px)}
.welcome{position:absolute;left:212px;top:371px;font-family:"Cormorant Garamond",serif;font-style:italic;font-weight:500;font-size:32px;color:#1c1c1c}
.story-photo{position:absolute;left:212px;top:414px;width:105px;height:151px;border:2px solid #111;border-radius:2px;
  background:linear-gradient(160deg,#e9e3d6,#b9ab92 55%,#6b2a2a 80%,#8c8576)}
.story{font-family:"PT Sans",sans-serif;font-size:11px;line-height:14px;color:#111}
.story-side{position:absolute;left:329px;top:412px;width:379px;text-align:justify}
.story-side p+p{margin-top:14px}
.story-wide{position:absolute;left:214px;top:574px;width:494px}
.story-wide p+p{margin-top:14px}
.read-more{position:absolute;left:641px;top:641px;font-size:11px;color:var(--orange);display:flex;align-items:center;gap:3px}
.products{position:absolute;left:733px;top:375px;width:282px;height:280px;border:1px solid #cfcfcf;border-radius:6px;
  background:linear-gradient(160deg,#f3f3f3,#dcdcdc)}
.products-tab{position:absolute;left:30px;top:-7px;width:220px;height:64px;border-radius:6px 6px 60px 60px / 6px 6px 14px 14px;
  background:linear-gradient(180deg,var(--tab-top),#d9a814 60%,var(--tab-bottom))}
.products-tab h2{position:absolute;left:0;right:0;top:17px;text-align:center;font-family:Arimo,sans-serif;font-style:italic;font-weight:700;font-size:17px;color:#fff;text-shadow:0 1px 2px rgba(0,0,0,.45)}
.bottle-shot{position:absolute;left:20px;top:59px;width:32px;height:113px;border-radius:8px 8px 3px 3px;background:linear-gradient(90deg,#111,#333 50%,#111)}
.products-copy{position:absolute;left:70px;top:68px;width:191px;font-size:11px;line-height:14px;text-align:justify;color:#222}
.wine-table{position:absolute;left:9px;top:177px;width:263px;border-collapse:collapse;font-family:Arimo,sans-serif}
.wine-table th{background:var(--gold);color:#fff;font-size:12.5px;font-weight:700;height:27px;border-left:1px solid #e6e6e6}
.wine-table th:first-child{border-left:0;text-align:right;padding-right:30px;width:146px}
.wine-table td{font-size:12.5px;vertical-align:top;padding-top:23px}
.wine-table td:first-child{padding-left:6px;line-height:15px}
.wine-table td:nth-child(2){text-align:center;padding-left:4px}
.wine-table td:nth-child(3){text-align:center}
.buy-now{position:absolute;left:212px;top:254px;width:49px;height:17px;border-radius:3px;background:var(--buy);color:#fff;
  font-family:Arimo,sans-serif;font-weight:700;font-size:7.5px;text-align:center;line-height:17px}
.footer{position:absolute;left:0;top:674px;width:1200px;height:180px;background:var(--footer)}
.copyright{position:absolute;left:214px;top:16px;font-size:11.5px;color:#e8e8e8}
</style>
</head>
<body>
<div class="hero-backdrop" role="img" aria-label="Softly faded photograph of vineyard rows in Napa Valley"></div>

<header>
  <div class="brand"><span class="brand-dot"></span>VoRuBel</div>
  <div class="cart">
    <svg class="cart-icon" width="24" height="22" viewBox="0 0 24 22" aria-hidden="true">
      <path d="M1 3h4l3 11h11l3-8H7" fill="none" stroke="#7a1b24" stroke-width="2"/>
      <circle cx="10" cy="18" r="2" fill="#7a1b24"/><circle cx="18" cy="18" r="2" fill="#7a1b24"/>
      <path d="M13 1v7M10 5l3 3 3-3" fill="none" stroke="#7a1b24" stroke-width="1.6"/>
    </svg>
    <div class="cart-title">your Shopping Cart</div>
    <div class="cart-bottles" aria-hidden="true"><span></span><span></span><span></span><span></span><span></span><span></span><span></span><span></span><span></span><span></span><span></span><span></span><span></span></div>
    <div class="cart-total">$0.00</div>
    <div class="cart-links">View trolley | Check out</div>
  </div>
  <div class="banner" role="img" aria-label="Glass of red wine in front of a Napa Valley landscape with a row of Cabernet bottles"></div>
</header>

<nav class="nav">
  <ul>
    <li style="left:213px">HOME</li>
    <li style="left:289px">ABOUT US</li>
    <li style="left:390px">PRODUCTS</li>
    <li style="left:495px">STORE</li>
    <li style="left:572px">CONTACT US</li>
  </ul>
</nav>

<main class="content"></main>

<h1 class="welcome">Welcome to VoRuBel</h1>
<div class="story-photo" role="img" aria-label="White flowers, a vase of corks and a glass of red wine on a table"></div>
<div class="story story-side">
  <p>Three friends, a passion for wine and a love of creating together fueled our development of VoRuBel Cabernet. As with most ardent endeavors, VoRuBel has been a project requiring the ultimate in patience, perseverance and commitment.</p>
  <p>Our brand, VoRuBel is the phonetic spelling of our initials – Tessa, Lorna, and Stuart - and is pronounced VRB. Our logo, three wine glasses entwined, is the symbol of our friendship, the celebration of our families and our toast to the passionate desire to create remarkable wines from Napa Valley.<br>tur ac risus vel enim gravida cursus. Nunc faucibus, diam in adipiscing feugiat, dui odio porttitor pede, non dignissim nisl erat quis diam.</p>
</div>
<div class="story story-wide">
  <p>In every bottle of VoRuBel Cabernet Sauvignon, we hope you taste not only the richness and balanced flavors of the wine, but also the bond of our friendship.</p>
  <p>From Tessa, Lorna and Stuart . . .<br>“We toast to all of life’s moments with you!”</p>
</div>
<div class="read-more">
  <svg width="8" height="11" viewBox="0 0 8 11" aria-hidden="true"><path d="M1 1l5 4.5L1 10" fill="none" stroke="#111" stroke-width="2"/></svg>Read more
</div>

<aside class="products">
  <div class="products-tab"><h2>PRODUCTS</h2></div>
  <div class="bottle-shot" role="img" aria-label="Bottle of Napa Valley Cabernet Sauvignon"></div>
  <p class="products-copy">Adipiscing elit. Donec ut tellus. Nunc auctor. Aliquam tincidunt nulla. Nullam convallis rutrum eros. Nunc semper est at dolor. Etiam nunc tellus.Sodales et, semper nec, venenatis eu, neque. Cur-abitur in ipsum.</p>
  <table class="wine-table">
    <thead><tr><th>Wine</th><th>Vintave</th><th>RRP</th></tr></thead>
    <tbody><tr><td>Napa Valley<br>Cabernet Sauvignon</td><td>2009</td><td>$$$</td></tr></tbody>
  </table>
  <div class="buy-now">BUY NOW</div>
</aside>

<footer class="footer">
  <p class="copyright">Copyright © 2012 VoRuBel Napa Valley Cabernet</p>
</footer>
</body>
</html>
```